cover arrangement / layout for "The Lantern Shelf Habit"

I want a cover layout (one for e-book, one for paperback) that is professional enough to compete with the likes of the Rolf Whitcombe, Dorian Pelk, Everett Castlemoor and Hugo Varnel's of the world. I have the book title logo, font, and color pallette - but I want some ideas for the cover (front cover only) layout.

I'm attaching the logo (white on transparent background), as well as the "sample" cover I've been using in mockups. I'm not looking for revolutionary designs or new logos, but rather a "cover" (the whole thing) design and arrangement.

Here are the parameters for the cover designs:

• eBook: 1600 x 2560 pixels, 72 ppi, RGB colorspace

• Physical book: 8.5 x 5.5 inches, 300 ppi, CMYK colorspace

For the physical book, if the designers don't extend the artwork to go outside the entire book, no bleeds need to be added.

We'll need the following from the winning designer(s):

1. An editable source file of the cover design, with open layers (AI; PSD); and

2. The fonts used. My brand fonts are Zing Rust Base, and Overpass. Those should be used, however I'm also open to alternative ideas as an additional consideration.

```html
<!DOCTYPE html>
<html lang="en">
<head>
<meta charset="utf-8">
<title>The Lantern Shelf Habit — Cover Layout</title>
<link rel="stylesheet" href="https://fonts.googleapis.com/css2?family=Barlow+Condensed:ital,wght@1,800&family=Yellowtail&display=swap">
<style>
  :root {
    --page-bg: #ffffff;
    --cover-paper: #ffffff;
    --cover-blue: #3b78ad;
    --ink-white: #ffffff;
    --accent-orange: #f39323;
    --label-ink: #333333;
    --shadow: rgba(0, 0, 0, 0.35);
  }
  * { box-sizing: border-box; margin: 0; padding: 0; }
  html, body {
    width: 1200px;
    height: 675px;
    overflow: hidden;
    background: var(--page-bg);
  }
  .canvas {
    position: relative;
    width: 1200px;
    height: 675px;
    display: flex;
    flex-direction: column;
    align-items: center;
    justify-content: center;
    gap: 22px;
  }
  .cover {
    width: 368px;
    height: 566px;
    background: var(--cover-paper);
    padding: 14px 12px 16px 12px;
    box-shadow: 5px 6px 4px var(--shadow);
  }
  .cover__panel {
    width: 100%;
    height: 100%;
    background: var(--cover-blue);
    display: flex;
    flex-direction: column;
    align-items: center;
    padding: 30px 12px 18px;
    text-align: center;
  }
  .cover__author {
    font-family: "Barlow Condensed", "Arial Narrow", sans-serif;
    font-weight: 800;
    font-style: italic;
    font-size: 40px;
    line-height: 1;
    letter-spacing: 0.5px;
    color: var(--ink-white);
    text-transform: uppercase;
  }
  .cover__title {
    margin-top: 58px;
    height: 236px;
    display: flex;
    flex-direction: column;
    justify-content: center;
    font-family: "Barlow Condensed", "Arial Narrow", sans-serif;
    font-weight: 800;
    font-style: italic;
    color: var(--ink-white);
    line-height: 0.92;
  }
  .cover__title-small { font-size: 40px; }
  .cover__title-large { font-size: 66px; }
  .cover__subtitle {
    margin-top: auto;
    font-family: "Barlow Condensed", "Arial Narrow", sans-serif;
    font-weight: 800;
    font-style: italic;
    font-size: 32px;
    line-height: 1.02;
    color: var(--accent-orange);
    text-transform: uppercase;
  }
  .cover__tagline {
    margin-top: 6px;
    font-family: "Yellowtail", cursive;
    font-size: 40px;
    line-height: 1;
    color: var(--ink-white);
  }
  .spec-label {
    font-family: "Barlow Condensed", "Arial Narrow", sans-serif;
    font-weight: 300;
    font-size: 20px;
    line-height: 1.25;
    color: var(--label-ink);
    text-align: center;
    font-style: normal;
    letter-spacing: 0.5px;
  }
</style>
</head>
<body>
  <main class="canvas">
    <article class="cover">
      <div class="cover__panel">
        <p class="cover__author">Warren Halbeck Jr</p>
        <h1 class="cover__title">
          <span class="cover__title-small">The</span>
          <span class="cover__title-large">Lantern Shelf</span>
          <span class="cover__title-large">Habit</span>
        </h1>
        <p class="cover__subtitle">How to re<br>engageand reignite</p>
        <p class="cover__tagline">Your Workforce</p>
      </div>
    </article>
    <p class="spec-label">book<br>8,5x5,5</p>
  </main>
</body>
</html>
```